First Reponders Promotion poster/flyer

Our Yoga studio is introducing an ongoing promotion for all First Responders, Police/Nurse/Paramedic/Firefighters/Doctors
$22pw for Unlimited access to our Inner city Studio which will become a sanctuary for the people who look after us. Tag line: You look after us, let us look after you. The benefits of yoga, reduce stress, clear mind, healthy body. Feel free to use other assets, and be as creative as you like I have just put images and designs as a guide.

Target Market(s)

Emergency Services Tasmania

Industry/Entity Type

Emergency Services

Requirements
Must have
• Solvaro Logo/Address 41 Kelmora St/ website www.solvarostudio.com.a/ sign up online and just bring in current work Id at checkin/$22pw Unlimited classes/Australian market so can't look like usa or any other countries
Nice to have
• words , inner city Sanctuary
Should not have
• Foreign Country images

```html
<!DOCTYPE html>
<html lang="en">
<head>
<meta charset="utf-8">
<title>Solvaro Studio – First Responders Offer</title>
<link href="https://fonts.googleapis.com/css2?family=Poppins:wght@400;500;700&family=Didact+Gothic&family=League+Spartan:wght@300;700&display=swap" rel="stylesheet">
<style>
  :root {
    --gold: #efae36;
    --maroon: #660000;
    --maroon-soft: #7a1a14;
    --ink: #000000;
    --paper: #ffffff;
    --rule: #e4e4e4;
  }
  * { margin: 0; padding: 0; box-sizing: border-box; }
  html, body { width: 848px; height: 1200px; overflow: hidden; background: var(--paper); }
  .poster { position: relative; width: 848px; height: 1200px; overflow: hidden; background: var(--paper); font-family: "Didact Gothic", sans-serif; }
  .abs { position: absolute; }

  .offer-band { left: 0; top: 350px; width: 848px; height: 222px; background: var(--gold); }
  .top-rule { left: 340px; top: 342px; width: 508px; height: 9px; background: var(--rule); }
  .decor { left: 0; top: 0; width: 848px; height: 1200px; }

  .brand { left: 380px; top: 96px; width: 424px; display: flex; align-items: center; justify-content: center; gap: 14px; }
  .brand-mark { width: 18px; height: 18px; background: var(--gold); }
  .brand-name { font-family: "Poppins", sans-serif; font-weight: 500; font-size: 46px; letter-spacing: 4px; color: var(--ink); line-height: 1; }

  .tagline { left: 370px; top: 205px; width: 446px; text-align: center; font-family: "League Spartan", sans-serif; font-weight: 300; font-size: 37px; line-height: 52px; color: var(--ink); }
  .tagline b { font-weight: 700; }

  .offer { left: 262px; top: 390px; width: 566px; text-align: center; font-size: 38px; line-height: 51px; color: var(--ink); }
  .offer .accent { font-family: "Poppins", sans-serif; font-weight: 700; color: var(--maroon); }
  .price-bar { left: 276px; top: 495px; width: 538px; height: 48px; background: var(--ink); color: var(--paper); font-family: "Poppins", sans-serif; font-weight: 700; font-size: 34px; line-height: 48px; text-align: center; }
  .price-bar .price { color: var(--gold); }

  .roles { left: 333px; top: 578px; width: 515px; height: 68px; background: var(--ink); color: var(--paper); font-family: "Poppins", sans-serif; font-weight: 700; font-size: 20px; line-height: 24px; text-align: center; padding-top: 9px; }

  .details { left: 333px; top: 646px; width: 515px; height: 420px; background: var(--maroon); }
  .address { left: 333px; top: 678px; width: 515px; text-align: center; font-family: "Poppins", sans-serif; font-weight: 700; font-size: 35px; line-height: 44px; color: var(--paper); }
  .address .from { font-weight: 400; }
  .address .date { color: var(--gold); font-weight: 700; }

  .figure-art { left: 358px; top: 802px; width: 140px; height: 212px; background: var(--maroon-soft); border-radius: 70px 70px 40px 40px; }
  .benefits { left: 509px; top: 796px; color: var(--paper); }
  .benefits h2 { font-family: "Poppins", sans-serif; font-weight: 700; font-size: 34px; color: var(--gold); line-height: 50px; }
  .benefits ul { list-style: none; margin-left: 12px; font-size: 28px; line-height: 43px; }
  .benefits li::before { content: "•"; margin-right: 10px; font-size: 18px; vertical-align: 3px; }

  .footer { left: 0; top: 1076px; width: 848px; height: 124px; background: var(--gold); text-align: center; }
  .footer-note { font-family: "Poppins", sans-serif; font-weight: 400; font-size: 19.5px; color: var(--ink); margin-top: 24px; white-space: nowrap; }
  .footer-note b { font-weight: 700; }
  .web { font-family: "Poppins", sans-serif; font-size: 25.5px; letter-spacing: 3.3px; color: var(--maroon); margin-top: 8px; }
  .web b { font-weight: 700; }
</style>
</head>
<body>
<main class="poster">
  <div class="abs offer-band"></div>
  <div class="abs top-rule"></div>

  <svg class="abs decor" width="848" height="1200" viewBox="0 0 848 1200">
    <defs>
      <linearGradient id="fireTone" x1="0" y1="0" x2="1" y2="1">
        <stop offset="0" stop-color="#b79a6e"/>
        <stop offset="0.5" stop-color="#8a6f4c"/>
        <stop offset="1" stop-color="#4b4036"/>
      </linearGradient>
      <linearGradient id="policeTone" x1="0" y1="0" x2="0" y2="1">
        <stop offset="0" stop-color="#5a5d66"/>
        <stop offset="0.45" stop-color="#9fb14a"/>
        <stop offset="1" stop-color="#c6d63c"/>
      </linearGradient>
    </defs>
    <polygon role="img" aria-label="Photo of a firefighter in helmet and breathing mask" points="0,0 262,0 350,352 282,373 0,452" fill="url(#fireTone)"/>
    <polygon points="0,452 282,373 282,378 0,458" fill="#ffffff"/>
    <line x1="262" y1="0" x2="285" y2="78" stroke="#000" stroke-width="8"/>
    <line x1="295" y1="200" x2="340" y2="358" stroke="#efae36" stroke-width="11"/>
    <line x1="286" y1="265" x2="318" y2="360" stroke="#efae36" stroke-width="11"/>
    <rect x="0" y="570" width="262" height="8" fill="#ffffff"/>
    <rect role="img" aria-label="Photo of a police officer in a high-visibility vest" x="0" y="578" width="333" height="498" fill="url(#policeTone)"/>
    <rect x="283" y="578" width="14" height="126" fill="#efae36"/>
    <rect x="306" y="578" width="14" height="187" fill="#efae36"/>
  </svg>

  <header class="abs brand">
    <span class="brand-mark"></span>
    <span class="brand-name">SOLVARO</span>
  </header>

  <p class="abs tagline">YOU LOOK <b>AFTER US,</b><br>LET US LOOK <b>AFTER YOU!</b></p>

  <p class="abs offer">Unlimited access to our classes<br>in our <span class="accent">beautiful inner-city</span></p>
  <div class="abs price-bar">Studio Sanctuary <span class="price">for $22pw</span></div>

  <div class="abs roles">PARAMEDIC | AMBULANCE | NURSE<br>POLICE | FIREFIGHTERS | SES | DOCTORS</div>

  <section class="abs details"></section>
  <p class="abs address">41 Kelmora St, Hobart<br><span class="from">from </span><span class="date">1st of July 2022</span></p>

  <div class="abs figure-art" role="img" aria-label="Line drawing of a person meditating in lotus pose"></div>

  <div class="abs benefits">
    <h2>Yoga helps you:</h2>
    <ul>
      <li>Reduce stress</li>
      <li>Clear your mind</li>
      <li>Have a healthy body</li>
    </ul>
  </div>

  <footer class="abs footer">
    <p class="footer-note">JUST <b>SIGN UP ON OUR WEBSITE</b> AND BRING IN YOUR <b>CURRENT ID</b> FOR VERIFICATION</p>
    <p class="web">www.<b>solvarostudio</b>.com</p>
  </footer>
</main>
</body>
</html>
```